Real Estate Sign Project

We need a Real Estate sign that promotes the property being listed and our company and agent listing the property. The images need to be able to be swapped out so we can use the template for each listing we have. I have a sample from another company that shows what were are trying to accomplish. Would want ours to be unique using our logo and the colors in our logo. We would like to not have to use a rider. Would want agents name and phone number to be part of the 36" x 24" sign.

Industry/Entity Type

Real Estate

Requirements
Must have
• Sign dimensions are 36 inches by 24 inches (36" across and 24" up down). Use example.of.sign.we.want.jpg as the direction we want to go but with a different layout and our logo and colors. This would be just a template that we can swap out new pictures, address, price, website, agents contact info for each home we are listing. Like the idea of the pictures bleeding off the sides. Please use free stock photos for the home images as we will be changing these out for each listing. Please incorporate all info including agents info into the one sign. File must be layered so we can change the pictures, price, website, agent, etc. We use GIMP (.xcf) file

```html
<!DOCTYPE html>
<html lang="en">
<head>
<meta charset="utf-8">
<title>Home For Sale – Listing Sign</title>
<link rel="stylesheet" href="https://fonts.googleapis.com/css2?family=Libre+Baskerville:wght@400;700&family=Open+Sans:wght@400;600;700&display=swap">
<style>
  :root {
    --orange: #f26a21;
    --blue: #1d5ea8;
    --blue-dark: #163f73;
    --white: #ffffff;
    --ink: #1d2430;
    --backdrop: #e8eaed;
  }
  * { box-sizing: border-box; margin: 0; padding: 0; }
  html, body { width: 1200px; height: 900px; overflow: hidden; }
  body {
    background: var(--backdrop);
    font-family: "Open Sans", Arial, sans-serif;
    color: var(--ink);
  }
  .sign {
    position: absolute;
    left: 60px; top: 90px;
    width: 1080px; height: 720px;
    background: var(--white);
    box-shadow: 0 10px 30px rgba(0,0,0,.14);
    overflow: hidden;
  }
  /* ---------- listing photos, bleeding off the left, top and bottom edges ---------- */
  .gallery { position: absolute; left: 0; top: 0; width: 690px; height: 720px; }
  .photo { position: absolute; }
  .photo--exterior {
    left: 0; top: 0; width: 690px; height: 306px;
    background: linear-gradient(180deg, #2f6fc4 0%, #7eb0e6 38%, #cdb89a 62%, #a88d6c 100%);
  }
  .photo--living {
    left: 0; top: 378px; width: 206px; height: 168px;
    background: linear-gradient(160deg, #d9c7a8 0%, #8a6a48 60%, #4e3a28 100%);
  }
  .photo--bath {
    left: 0; top: 552px; width: 206px; height: 168px;
    background: linear-gradient(160deg, #b9926a 0%, #7a5234 60%, #3f2a1a 100%);
  }
  .photo--kitchen {
    left: 212px; top: 378px; width: 250px; height: 342px;
    background: linear-gradient(170deg, #e6d8c0 0%, #b27a45 45%, #8a5630 75%, #d7c9b3 100%);
  }
  .photo--dining {
    left: 468px; top: 378px; width: 222px; height: 342px;
    background: linear-gradient(170deg, #efe6d4 0%, #c9a77c 50%, #8c6844 100%);
  }
  .details-band {
    position: absolute; left: 0; top: 306px; width: 704px; height: 66px;
    background: var(--blue-dark);
    display: flex; align-items: center;
    clip-path: polygon(0 0, 100% 0, 96% 100%, 0 100%);
  }
  .details-band__address {
    height: 100%; padding: 0 22px;
    display: flex; align-items: center;
    background: var(--blue);
    color: var(--white); font-size: 24px; font-weight: 600;
    white-space: nowrap;
  }
  .details-band__specs {
    padding-left: 22px; color: var(--white);
    font-size: 15px; line-height: 1.45; white-space: nowrap;
  }
  /* ---------- brand panel, bleeding off the right, top and bottom edges ---------- */
  .panel { position: absolute; left: 696px; top: 0; width: 384px; height: 720px; }
  .panel__headline {
    position: absolute; left: 0; top: 0; width: 100%; height: 270px;
    background: var(--orange); color: var(--white);
    font-family: "Libre Baskerville", Georgia, serif;
    font-weight: 400;
    text-align: center; padding-top: 44px;
  }
  .panel__headline .big { display: block; font-size: 66px; line-height: 1.05; }
  .panel__headline .small { display: block; font-size: 40px; line-height: 1.3; }
  .panel__brand {
    position: absolute; left: 0; top: 230px; width: 100%; height: 250px;
    background: var(--white);
    clip-path: polygon(0 40px, 42% 40px, 50% 0, 58% 40px, 100% 40px, 100% 210px, 58% 210px, 50% 250px, 42% 210px, 0 210px);
    display: flex; flex-direction: column; align-items: center; justify-content: center;
  }
  .brand-name {
    display: flex; align-items: center; gap: 10px;
    color: var(--blue); font-weight: 700; font-size: 40px; letter-spacing: 1px;
  }
  .brand-name__dot { width: 22px; height: 22px; border-radius: 50%; background: var(--orange); }
  .brand-web { margin-top: 8px; color: var(--blue-dark); font-size: 17px; font-weight: 600; }
  .panel__contact {
    position: absolute; left: 0; top: 440px; width: 100%; height: 280px;
    background: var(--orange); color: var(--white);
    padding: 72px 30px 0;
  }
  .price {
    font-family: "Libre Baskerville", Georgia, serif;
    font-size: 38px; white-space: nowrap;
  }
  .agent { margin-top: 26px; font-size: 24px; display: flex; align-items: center; }
  .agent__label { padding-right: 14px; border-right: 2px solid var(--white); margin-right: 14px; }
  .agent__name { font-weight: 700; }
  .phone { margin-top: 22px; font-size: 26px; font-weight: 600; }
</style>
</head>
<body>
  <main class="sign">
    <section class="gallery">
      <div class="photo photo--exterior" role="img" aria-label="Front exterior photo of the two-storey listed home"></div>
      <div class="details-band">
        <span class="details-band__address">1487 Larkspur Lane</span>
        <span class="details-band__specs">4 Bedrooms | 3.5 Baths | 3200 Finished SF<br>2-Car Garage</span>
      </div>
      <div class="photo photo--living" role="img" aria-label="Living room photo"></div>
      <div class="photo photo--bath" role="img" aria-label="Bathroom photo"></div>
      <div class="photo photo--kitchen" role="img" aria-label="Kitchen photo"></div>
      <div class="photo photo--dining" role="img" aria-label="Dining area photo"></div>
    </section>
    <section class="panel">
      <h1 class="panel__headline"><span class="big">HOME</span><span class="small">FOR SALE</span></h1>
      <div class="panel__brand">
        <div class="brand-name"><span class="brand-name__dot"></span>KEYSTEAD</div>
        <div class="brand-web">www.keysteadhomes.com</div>
      </div>
      <div class="panel__contact">
        <p class="price">$ 250,000 Only</p>
        <p class="agent"><span class="agent__label">Agent</span><span class="agent__name">Dale Mercer</span></p>
        <p class="phone">555/010-2741</p>
      </div>
    </section>
  </main>
</body>
</html>
```